Billboard design for property management

DEADLINE 3RD APRIL 2022
I need a billboard design sized 390cm x 275 cm with 10cm bleed.

It needs to attract potential homeowners who want to make money by renting out their property to holidays

White background with orange and grey (as in the logo) maybe with an image. It must somehow, incorporate the boost your bookings attached.

Needs to show web address and phone number

```html
<!DOCTYPE html>
<html lang="en">
<head>
<meta charset="utf-8">
<title>Keystone Property Management – Billboard</title>
<link rel="stylesheet" href="https://fonts.googleapis.com/css2?family=Montserrat:ital,wght@0,400;0,500;0,600;0,700;0,800;1,700&display=swap">
<style>
  :root {
    --orange: #e8782a;
    --grey: #54585a;
    --ink: #4a4d50;
    --white: #ffffff;
    --photo-sky: #6f8fc0;
    --photo-house: #4d5a7a;
    --photo-warm: #c98b45;
    --keys-metal: #d9d4c8;
    --keys-wood: #d6b184;
  }
  * { margin: 0; padding: 0; box-sizing: border-box; }
  html, body { width: 1200px; height: 904px; overflow: hidden; background: var(--white); }
  .billboard {
    position: relative;
    width: 1200px;
    height: 904px;
    overflow: hidden;
    background: var(--white);
    font-family: "Montserrat", Arial, sans-serif;
    color: var(--ink);
  }
  .billboard__shapes { position: absolute; inset: 0; }

  .brand {
    position: absolute;
    left: 69px;
    top: 62px;
    display: flex;
    align-items: center;
    gap: 16px;
  }
  .brand__dot {
    width: 70px; height: 70px;
    border-radius: 50%;
    background: var(--orange);
  }
  .brand__name {
    color: var(--orange);
    font-weight: 800;
    line-height: 1;
    text-transform: uppercase;
  }
  .brand__name span { display: block; }
  .brand__main { font-size: 52px; letter-spacing: 0.5px; }
  .brand__sub { font-size: 17px; margin-top: 8px; letter-spacing: 0.2px; }

  .headline {
    position: absolute;
    left: 68px;
    top: 206px;
    width: 580px;
    font-size: 66px;
    line-height: 76px;
    letter-spacing: 0;
    text-transform: uppercase;
    white-space: nowrap;
  }
  .headline__line { display: block; font-weight: 500; color: var(--ink); }
  .headline__accent { font-weight: 800; color: var(--orange); }

  .values {
    position: absolute;
    left: 70px;
    top: 455px;
    font-size: 31px;
    font-weight: 600;
    color: var(--ink);
    letter-spacing: 0.3px;
    white-space: nowrap;
  }
  .values__sep { color: var(--orange); font-weight: 500; margin: 0 8px; }

  .offer {
    position: absolute;
    left: 69px;
    top: 551px;
    width: 417px;
    height: 56px;
    border: 1.5px solid var(--orange);
    border-right: none;
    border-radius: 28px 0 0 28px;
    display: flex;
    align-items: center;
    padding-left: 22px;
    font-size: 38px;
    font-weight: 700;
    font-style: italic;
    color: var(--orange);
    letter-spacing: -0.3px;
    white-space: nowrap;
  }

  .contact {
    position: absolute;
    left: 75px;
    top: 758px;
    color: var(--white);
    white-space: nowrap;
  }
  .contact__lead { font-size: 35px; font-weight: 400; letter-spacing: 1px; }
  .contact__phone { font-size: 45px; font-weight: 700; letter-spacing: 1.5px; margin-top: 6px; }
  .website {
    position: absolute;
    left: 522px;
    top: 824px;
    font-size: 36px;
    font-weight: 700;
    color: var(--white);
    letter-spacing: 0.3px;
    white-space: nowrap;
  }

  .badge {
    position: absolute;
    left: 916px;
    top: 645px;
    width: 212px;
    height: 212px;
    border-radius: 50%;
    background: var(--orange);
    color: var(--white);
    display: flex;
    flex-direction: column;
    align-items: center;
    justify-content: center;
    text-transform: uppercase;
    line-height: 1;
    font-weight: 800;
    text-align: center;
  }
  .badge__big { font-size: 38px; }
  .badge__mid { font-size: 19px; margin-top: 4px; }
  .badge__small { font-size: 10px; margin: 6px 0; letter-spacing: 2px; border-top: 1.5px solid var(--white); border-bottom: 1.5px solid var(--white); padding: 2px 14px; }
  .badge__name { font-size: 20px; }
</style>
</head>
<body>
<main class="billboard">
  <svg class="billboard__shapes" viewBox="0 0 1200 904" width="1200" height="904">
    <defs>
      <linearGradient id="houseTones" x1="0" y1="0" x2="0.3" y2="1">
        <stop offset="0" stop-color="#6f8fc0"/>
        <stop offset="0.45" stop-color="#4d5a7a"/>
        <stop offset="0.8" stop-color="#c98b45"/>
        <stop offset="1" stop-color="#9aa0a0"/>
      </linearGradient>
      <linearGradient id="keyTones" x1="0" y1="0" x2="1" y2="1">
        <stop offset="0" stop-color="#d9d4c8"/>
        <stop offset="1" stop-color="#d6b184"/>
      </linearGradient>
    </defs>

    <path class="photo-frame" d="M800 0 C700 60 640 200 658 330 C676 480 790 620 930 700 L1200 700 L1200 0 Z" fill="#e8782a"/>
    <path class="photo" role="img" aria-label="Photo of a modern two-storey holiday home with lit windows at dusk"
          d="M836 0 C735 70 670 200 676 330 C684 470 790 610 928 700 L1200 712 L1200 0 Z" fill="url(#houseTones)"/>
    <path class="photo-sweep" d="M900 690 C980 712 1100 705 1200 626 L1200 720 L900 760 Z" fill="#ffffff"/>

    <path class="band-edge" d="M0 729 C90 690 170 672 250 672 C420 672 560 730 700 762 C780 780 860 790 930 785 C1030 778 1120 740 1200 690 L1200 904 L0 904 Z" fill="#e8782a"/>
    <path class="band" d="M0 750 C90 712 170 693 250 693 C420 693 560 752 700 780 C780 796 860 805 930 800 C1030 793 1120 752 1200 712 L1200 904 L0 904 Z" fill="#54585a"/>

    <path class="keys" role="img" aria-label="Photo of a bunch of house keys on a wooden house-shaped keyring"
          d="M490 540 L560 505 L620 560 L650 600 L700 650 L706 700 L660 727 L615 690 L600 640 L560 620 L500 592 Z" fill="url(#keyTones)"/>
  </svg>

  <div class="brand">
    <div class="brand__dot"></div>
    <div class="brand__name">
      <span class="brand__main">Keystone</span>
      <span class="brand__sub">Property Management Ltd</span>
    </div>
  </div>

  <h1 class="headline">
    <span class="headline__line">Rent <span class="headline__accent">Your</span></span>
    <span class="headline__line headline__accent">Property</span>
    <span class="headline__line">With Keystone</span>
  </h1>

  <p class="values">Professional<span class="values__sep">|</span>Honest<span class="values__sep">|</span>Reliable</p>

  <p class="offer">Low Commissions</p>

  <div class="contact">
    <p class="contact__lead">Call us today on</p>
    <p class="contact__phone">+357 99 482 617</p>
  </div>
  <p class="website">www.keystone.cy</p>

  <div class="badge">
    <span class="badge__big">Boost</span>
    <span class="badge__mid">Your Bookings</span>
    <span class="badge__small">With</span>
    <span class="badge__name">Keystone</span>
  </div>
</main>
</body>
</html>
```